Our companies name is The Gilded Ladle and we specialize in craft cupcakes, what I mean by that is that we bake our cupcakes with craft beer and other alcoholic drinks. We are trying to focus on being elegant but at the same time unpretentious. Since we are incorporating beer in our cupcakes we want the business card to have our logo in the front and our information in the back.

Once we select the best design we will provide the contact information to be added. Thank you.

Industry/Entity Type

Business

Font styles to use
Decorative
Script

Requirements
Must have
• Round corners
Should not have
• Square corners

```html
<!DOCTYPE html>
<html lang="en">
<head>
<meta charset="utf-8">
<title>The Gilded Ladle – Business Card</title>
<link href="https://fonts.googleapis.com/css2?family=Ubuntu:wght@400;500;700&display=swap" rel="stylesheet">
<style>
  :root {
    --backdrop: #1c1c1c;
    --card-red: #e8232a;
    --card-red-deep: #c4161c;
    --paper: #ffffff;
    --paper-shade: #ececec;
    --ink: #111111;
    --ink-soft: #2b2b2b;
    --accent-red: #e8232a;
    --accent-mint: #9fd8c4;
    --seal-white: #ffffff;
  }
  * { box-sizing: border-box; margin: 0; padding: 0; }
  html, body {
    width: 1200px;
    height: 1000px;
    overflow: hidden;
    background: var(--backdrop);
    font-family: "Ubuntu", sans-serif;
  }
  .canvas {
    width: 1200px;
    height: 1000px;
    display: flex;
    flex-direction: column;
    align-items: center;
    justify-content: center;
    gap: 60px;
  }
  .card {
    position: relative;
    width: 700px;
    height: 400px;
    border-radius: 22px;
    overflow: hidden;
  }

  /* Front */
  .card-front {
    background: radial-gradient(circle at 45% 45%, var(--card-red) 0%, var(--card-red) 45%, var(--card-red-deep) 100%);
    display: flex;
    align-items: center;
    justify-content: center;
  }
  .seal {
    width: 300px;
    height: 300px;
    border-radius: 50%;
    background: var(--seal-white);
    display: flex;
    align-items: center;
    justify-content: center;
  }
  .brand-name {
    font-family: "Ubuntu", sans-serif;
    font-weight: 700;
    color: var(--ink);
    text-align: center;
    line-height: 1.1;
  }
  .seal .brand-name { font-size: 34px; }

  /* Back */
  .card-back {
    background: linear-gradient(160deg, var(--paper) 0%, var(--paper) 55%, var(--paper-shade) 100%);
  }
  .red-rule {
    position: absolute;
    left: 34px;
    top: 62px;
    width: 8px;
    height: 180px;
    background: var(--accent-red);
  }
  .holder-name {
    position: absolute;
    left: 80px;
    top: 70px;
    font-weight: 700;
    font-size: 24px;
    color: var(--ink);
  }
  .holder-title {
    position: absolute;
    left: 80px;
    top: 104px;
    font-size: 17px;
    color: var(--ink-soft);
  }
  .mint-rule {
    position: absolute;
    left: 250px;
    top: 122px;
    width: 450px;
    height: 3px;
    background: var(--accent-mint);
  }
  .contact-list {
    position: absolute;
    left: 80px;
    top: 170px;
    list-style: none;
    font-size: 18px;
    color: var(--ink-soft);
    line-height: 33px;
  }
  .contact-list .label { margin-right: 4px; }
  .back-brand {
    position: absolute;
    right: 40px;
    bottom: 50px;
    width: 220px;
    display: flex;
    align-items: center;
    gap: 12px;
  }
  .back-brand .dot {
    flex: none;
    width: 26px;
    height: 26px;
    border-radius: 50%;
    background: var(--accent-red);
  }
  .back-brand .brand-name { font-size: 26px; text-align: left; }
</style>
</head>
<body>
  <main class="canvas">
    <section class="card card-front" aria-label="Card front">
      <div class="seal">
        <p class="brand-name">The Gilded<br>Ladle</p>
      </div>
    </section>

    <section class="card card-back" aria-label="Card back">
      <div class="red-rule"></div>
      <h1 class="holder-name">Cardholder Name</h1>
      <p class="holder-title">CEO &amp; Founder</p>
      <div class="mint-rule"></div>
      <ul class="contact-list">
        <li><span class="label">add:</span>your address goes here</li>
        <li><span class="label">p :</span>000 0123 456</li>
        <li><span class="label">e :</span>emailid@gildedladle.com</li>
        <li><span class="label">w :</span>www.gildedladle.com</li>
      </ul>
      <div class="back-brand">
        <span class="dot"></span>
        <p class="brand-name">The Gilded Ladle</p>
      </div>
    </section>
  </main>
</body>
</html>
```